update Coffeeshop menu design to be more modern and luxury

I want a menu that compliments the colors of the shop. I want a simple nice clean modern looking menu. The text is available on old menu (drinks) and the word document attached (food)

We changed the interior of our shop and want the new menu to reflect the new look and feel (see pictures attached). This project is a template menu therefore it should give us the ability to add content. Keep in mind that we want the layout to be one page . one side in english and the other in Arabic (we will update the arabic side to match the english design)
Updates

Project Deadline Extended
Reason: Now more information is provided including text and samples on old menu. The brand name is Brewvant.

Industry/Entity Type

Coffee Shop

Font styles to use
Sans Serif

Colors

Designer to choose colors to be used in the design.

Requirements
Must have
• My menu must have clean modern look that matches the shop style. It should have the logo of the coffee shop (provided). we would like a one pager menu one ideally (double sided) with variant in a3 and a4
• The design will be a template that we can update with content (content is not final). I attached the current menu for reference although content will be changed.
Nice to have
• Simple, attractive, easy to read, luxury modern.
Should not have
• Should not be crowded. no folds. no need for images. should not look like the old menu

```html
<!DOCTYPE html>
<html lang="en">
<head>
<meta charset="UTF-8">
<title>Brewvant Menu</title>
<link href="https://fonts.googleapis.com/css2?family=Playfair+Display:wght@700;900&family=PT+Serif:wght@400;700&display=swap" rel="stylesheet">
<style>
  :root {
    --cream: #f4ece1;
    --brown: #5a3220;
    --dark: #2f1910;
    --tan: #c99a6b;
    --orange: #d07a2e;
    --ink: #3a2418;
    --light: #f8efe4;
  }
  * { margin: 0; padding: 0; box-sizing: border-box; }
  html, body { width: 849px; height: 1200px; overflow: hidden; background: var(--cream); }
  .menu {
    position: relative; width: 849px; height: 1200px; overflow: hidden;
    background: var(--cream); font-family: "PT Serif", serif; color: var(--ink);
  }
  .backdrop { position: absolute; inset: 0; }
  .block { position: absolute; }
  .brand {
    position: absolute; left: 230px; top: 14px; width: 128px; height: 128px;
    border-radius: 50%; background: var(--brown);
    display: flex; align-items: center; justify-content: center;
  }
  .brand-name { font-family: "PT Serif", serif; font-weight: 700; font-size: 22px; color: var(--light); }
  .title-cold {
    position: absolute; left: 22px; top: 150px; width: 260px;
    font-family: "Playfair Display", serif; font-weight: 900; font-size: 44px;
    line-height: 1; color: var(--orange);
  }
  .section-title { font-family: "Playfair Display", serif; font-weight: 700; font-size: 27px; line-height: 1.1; }
  .on-dark { color: var(--light); }
  .on-light { color: var(--brown); }
  .list { display: grid; grid-template-columns: 1fr 44px 44px; font-size: 12.5px; row-gap: 2px; margin-top: 6px; }
  .list.single { grid-template-columns: 1fr 50px; }
  .list .head { font-size: 11px; text-align: center; }
  .list .price { text-align: center; }
  .list .note { display: block; font-size: 8px; opacity: .85; }
  .food-word {
    position: absolute; left: 568px; top: 18px; writing-mode: vertical-rl;
    font-family: "Playfair Display", serif; font-weight: 900; font-size: 92px;
    line-height: 1; letter-spacing: 4px; color: var(--brown);
  }
  .food { position: absolute; left: 682px; top: 16px; width: 158px; }
  .food-item { margin-bottom: 10px; }
  .food-item h3 { font-weight: 700; font-size: 14px; color: var(--brown); letter-spacing: .3px; line-height: 1.2; }
  .food-item p { font-size: 11px; line-height: 1.3; }
  .drinks-word {
    position: absolute; left: 300px; top: 610px;
    font-family: "Playfair Display", serif; font-weight: 900; font-size: 62px;
    line-height: 1; color: var(--brown); letter-spacing: 2px;
  }
  .cup { position: absolute; left: 320px; top: 440px; width: 150px; height: 150px; border-radius: 50%;
    background: radial-gradient(circle, #6b3f27 0%, #a8764f 45%, #efe3d4 72%, var(--cream) 100%); }
</style>
</head>
<body>
<main class="menu">
  <svg class="backdrop" width="849" height="1200" viewBox="0 0 849 1200" aria-hidden="true">
    <defs>
      <linearGradient id="interior" x1="0" y1="0" x2="1" y2="0">
        <stop offset="0" stop-color="#4a2c1d"/>
        <stop offset=".65" stop-color="#6d4a35"/>
        <stop offset="1" stop-color="#f4ece1" stop-opacity="0"/>
      </linearGradient>
    </defs>
    <rect x="0" y="130" width="330" height="620" fill="url(#interior)" role="img" aria-label="Photo of the cafe interior"/>
    <path d="M0,745 C100,728 200,715 290,705 L290,735 C200,760 100,815 0,850 Z" fill="var(--dark)"/>
    <path d="M0,872 C100,842 200,772 290,748" stroke="var(--orange)" stroke-width="3" fill="none"/>
  </svg>

  <div class="brand"><span class="brand-name">Brewvant</span></div>

  <div class="food-word">FOOD</div>

  <section class="food">
    <div class="food-item"><h3>SANDWICHES: -</h3><p>Selection of Fresh Sandwiches from our in-house kitchen</p></div>
    <div class="food-item"><h3>SALADS: -</h3><p>Variety of Salads for healthy living and fit body</p></div>
    <div class="food-item"><h3>CROISSANT: -</h3><p>Assorted flavors like chocolate, cheese, zatar and almond made to class from our baker</p></div>
    <div class="food-item"><h3>MUFFIN and COOKIES: -</h3><p>Wide range of muffins and cookies to select from our in-house bakery</p></div>
    <div class="food-item"><h3>CAKES: -</h3><p>Wide ranges of cakes baked by our own pastry chef</p></div>
  </section>

  <h1 class="title-cold">Cold Beverages</h1>

  <section class="block" style="left:22px; top:262px; width:280px;">
    <h2 class="section-title on-dark">Coffee On Ice</h2>
    <div class="list on-dark">
      <span></span><span class="head">Regular</span><span class="head">Double</span>
      <span>Iced Americano</span><span class="price">17</span><span class="price">19</span>
      <span>Iced Cappuccino</span><span class="price">17</span><span class="price">19</span>
      <span>Iced Latte</span><span class="price">19</span><span class="price">21</span>
      <span>Iced Caramel Macchiato</span><span class="price">19</span><span class="price">21</span>
      <span>Iced Mocha</span><span class="price">19</span><span class="price">21</span>
      <span>Iced Chocolate</span><span class="price">19</span><span class="price">21</span>
      <span>Iced Milk</span><span class="price">13</span><span class="price">-</span>
      <span>Iced Shaken Espresso</span><span class="price">17</span><span class="price">-</span>
    </div>
  </section>

  <section class="block" style="left:22px; top:505px; width:270px;">
    <h2 class="section-title on-dark">Iced Gourmet Tea</h2>
    <div class="list on-dark">
      <span></span><span class="head">Small</span><span class="head">Double</span>
      <span>Iced Green Tea</span><span class="price">13</span><span class="price">17</span>
      <span>Iced Green Tea<span class="note">with Honey Lemon</span></span><span class="price">15</span><span class="price">17</span>
      <span>Iced Chamomile</span><span class="price">13</span><span class="price">17</span>
      <span>Iced Cucumber<span class="note">Hibiscus Tea</span></span><span class="price">15</span><span class="price">17</span>
      <span>Iced Peach Tea</span><span class="price">13</span><span class="price">17</span>
      <span>Iced Lemon Tea</span><span class="price">13</span><span class="price">17</span>
    </div>
  </section>

  <div class="cup" role="img" aria-label="Illustration of a coffee cup with beans"></div>
  <div class="drinks-word">DRINKS</div>

  <section class="block" style="left:580px; top:462px; width:250px;">
    <h2 class="section-title on-light">Juices &amp; Frosties</h2>
    <div class="list">
      <span></span><span class="head">Regular</span><span class="head">Double</span>
      <span>Citrus Frostie</span><span class="price">17</span><span class="price">19</span>
      <span>Strawberry Frostie</span><span class="price">21</span><span class="price">23</span>
      <span>Lychee Frostie</span><span class="price">19</span><span class="price">21</span>
      <span>Orange Juice</span><span class="price">17</span><span class="price">19</span>
      <span>Lemon and Mint Juice</span><span class="price">13</span><span class="price">13</span>
    </div>
  </section>

  <section class="block" style="left:580px; top:615px; width:250px;">
    <h2 class="section-title on-light">Frappevant</h2>
    <div class="list">
      <span></span><span class="head">Regular</span><span class="head">Double</span>
      <span>Coffee Frapped</span><span class="price">17</span><span class="price">20</span>
      <span>Dark Mocha Frappevant</span><span class="price">20</span><span class="price">22</span>
      <span>Chocolate Frappevant</span><span class="price">20</span><span class="price">22</span>
      <span>Vanilla Frappevant</span><span class="price">20</span><span class="price">22</span>
      <span>Mango Frappevant</span><span class="price">20</span><span class="price">22</span>
      <span>Strawberry Frappevant</span><span class="price">21</span><span class="price">23</span>
      <span>Double Mocha Frappevant</span><span class="price">20</span><span class="price">22</span>
      <span>Cookies and Cream Frappevant</span><span class="price">20</span><span class="price">22</span>
      <span>Coffee Crumble Frappevant</span><span class="price">20</span><span class="price">22</span>
    </div>
  </section>

  <section class="block" style="left:580px; top:870px; width:250px;">
    <h2 class="section-title on-light">Adding Variety &amp; Extras</h2>
    <div class="list single">
      <span></span><span class="head">Regular</span>
      <span>Italian Soda<span class="note">(Strawberry / Lychee / Lime)</span></span><span class="price">17</span>
      <span>Spring Water</span><span class="price">10</span>
      <span>Brewvant Water</span><span class="price">5</span>
      <span>Sparkling Water</span><span class="price">10</span>
      <span>Extra Shot</span><span class="price">6</span>
      <span>Syrup<span class="note">(Vanilla / Caramel / Hazelnut)</span></span><span class="price">4</span>
      <span>Whipped Cream</span><span class="price">4</span>
      <span>Chocolate Sauce</span><span class="price">4</span>
      <span>Caramel Sauce</span><span class="price">4</span>
      <span>Almond Milk</span><span class="price">6</span>
      <span>Soya Milk</span><span class="price">6</span>
    </div>
  </section>

  <section class="block" style="left:300px; top:740px; width:255px;">
    <h2 class="section-title on-light">Hot Beverage</h2>
    <div class="list">
      <span></span><span class="head">Small</span><span class="head">Double</span>
      <span>Espresso</span><span class="price">11</span><span class="price">13</span>
      <span>Espresso Con Panna</span><span class="price">16</span><span class="price">18</span>
      <span>Espresso Macchiato</span><span class="price">13</span><span class="price">15</span>
      <span>Turkish Coffee</span><span class="price">11</span><span class="price">13</span>
    </div>
  </section>

  <section class="block" style="left:300px; top:900px; width:255px;">
    <h2 class="section-title on-light">Gourmet Tea</h2>
    <div class="list">
      <span></span><span class="head">Regular</span><span class="head">Double</span>
      <span>English Breakfast Tea</span><span class="price">13</span><span class="price"></span>
      <span>Earl Grey Tea</span><span class="price">13</span><span class="price"></span>
      <span>Peppermint Tea</span><span class="price">13</span><span class="price"></span>
      <span>Camomile Tea</span><span class="price">13</span><span class="price"></span>
      <span>Green Tea</span><span class="price">13</span><span class="price"></span>
      <span>Chai Tea Latte</span><span class="price">13</span><span class="price">21</span>
    </div>
  </section>

  <section class="block" style="left:22px; top:900px; width:250px;">
    <h2 class="section-title on-light">Hot Coffee</h2>
    <div class="list">
      <span></span><span class="head">Regular</span><span class="head">Double</span>
      <span>Americano</span><span class="price">15</span><span class="price">17</span>
      <span>Cappuccino</span><span class="price">17</span><span class="price">19</span>
      <span>Cafe Latte</span><span class="price">17</span><span class="price">19</span>
      <span>Dark Mocha</span><span class="price">19</span><span class="price">21</span>
      <span>Caramel Macchiato</span><span class="price">19</span><span class="price">21</span>
      <span>Hot Chocolate</span><span class="price">19</span><span class="price">21</span>
      <span>Flat White</span><span class="price">17</span><span class="price">-</span>
      <span>Arabic Coffee</span><span class="price">15</span><span class="price">17</span>
      <span>Hot Milk</span><span class="price">10</span><span class="price">-</span>
      <span>Tiramisu Latte</span><span class="price">19</span><span class="price">21</span>
      <span>Double Mocha</span><span class="price">19</span><span class="price">21</span>
    </div>
  </section>
</main>
</body>
</html>
```